Corvane Electrical Solutions

On one side. LOGO (underneath:) Commercial Industrial Residential

- NAME & CONTACT DETAILS

Marcus T. Hollings
Project Manager

(Cell icon) (441) 582-6197
(Email icon) cvnelectricalsoultions@mailventra.com
(Facebook & Instagram icons )@cvnelectricalsolutions

Other side: LOGO - underneath ELECTRICAL CONSTRUCTION & MAINTENANCE . LED LIGHTING & AUTOMATION . LIFE SAFETY SYSTEMS (FIRE ALARM / SECURITY) . DATA & COMMUNICATION

```html
<!DOCTYPE html>
<html lang="en">
<head>
<meta charset="utf-8">
<title>Corvane Electrical Solutions – Business Card</title>
<link rel="stylesheet" href="https://fonts.googleapis.com/css2?family=Montserrat:wght@400;500;600;700&family=Arimo:wght@400&display=swap">
<style>
  :root {
    --backdrop: #ababab;
    --teal: #0e5468;
    --paper: #ffffff;
    --ink-grey: #555a5e;
    --white: #ffffff;
  }
  * { box-sizing: border-box; margin: 0; padding: 0; }
  html, body { width: 1200px; height: 1055px; overflow: hidden; }
  body {
    background: var(--backdrop);
    font-family: "Montserrat", sans-serif;
    position: relative;
  }
  .card {
    position: absolute;
    top: 182px;
    width: 375px;
    height: 656px;
  }
  .card--front { left: 181px; background: var(--teal); color: var(--white); text-align: center; }
  .card--back { left: 647px; background: var(--paper); }

  .brand-name {
    font-weight: 600;
    text-transform: uppercase;
    letter-spacing: 1.5px;
    line-height: 1.1;
  }
  .card--front .brand {
    position: absolute; top: 44px; left: 0; right: 0;
    display: flex; justify-content: center; align-items: center; gap: 10px;
  }
  .card--front .brand-name { font-size: 17px; text-align: left; }
  .brand-mark { width: 14px; height: 14px; background: currentColor; flex: none; }
  .sectors {
    position: absolute; top: 112px; left: 0; right: 0;
    font-size: 11.5px; font-weight: 500; letter-spacing: 0.3px;
  }
  .sectors .dot { display: inline-block; width: 4px; height: 4px; border-radius: 50%; background: var(--white); vertical-align: middle; margin: 0 4px; }

  .person { position: absolute; top: 424px; left: 0; right: 0; }
  .person-name { font-size: 22px; font-weight: 700; letter-spacing: 0.5px; }
  .person-role { font-size: 15px; font-weight: 600; margin-top: 3px; }

  .contact-icons {
    position: absolute; top: 493px; left: 0; right: 0;
    display: flex; justify-content: center; gap: 7px;
  }
  .contact-icons svg { width: 26px; height: 26px; }
  .contact-lines {
    position: absolute; top: 540px; left: 0; right: 0;
    font-size: 14px; line-height: 21px;
  }

  .card--back .brand {
    position: absolute; top: 208px; left: 0; right: 0;
    display: flex; justify-content: center; align-items: center; gap: 10px;
    color: var(--teal);
  }
  .card--back .brand-name { font-size: 19px; }
  .services {
    position: absolute; top: 325px; left: 43px;
    list-style: none;
    font-family: "Arimo", sans-serif;
    font-size: 14.5px; line-height: 18.5px;
    color: var(--ink-grey);
  }
  .services li { position: relative; padding-left: 15px; }
  .services li::before {
    content: ""; position: absolute; left: 0; top: 6px;
    width: 6px; height: 6px; border-radius: 50%; background: var(--teal);
  }
</style>
</head>
<body>
  <section class="card card--front">
    <div class="brand">
      <span class="brand-mark"></span>
      <span class="brand-name">Corvane<br>Electrical<br>Solutions</span>
    </div>
    <p class="sectors">COMMERCIAL<span class="dot"></span>INDUSTRIAL<span class="dot"></span>RESIDENTIAL</p>

    <div class="person">
      <h1 class="person-name">MARCUS T. HOLLINGS</h1>
      <p class="person-role">Project Manager</p>
    </div>

    <div class="contact-icons">
      <svg viewBox="0 0 26 26" aria-label="Phone">
        <circle cx="13" cy="13" r="12" fill="none" stroke="#fff" stroke-width="1.2"/>
        <rect x="9.5" y="6.5" width="7" height="13" rx="1.3" fill="none" stroke="#fff" stroke-width="1.3"/>
        <line x1="12" y1="17.3" x2="14" y2="17.3" stroke="#fff" stroke-width="1.2"/>
      </svg>
      <svg viewBox="0 0 26 26" aria-label="Email">
        <circle cx="13" cy="13" r="12" fill="none" stroke="#fff" stroke-width="1.2"/>
        <rect x="7.5" y="9" width="11" height="8" rx="1" fill="#fff"/>
        <polyline points="7.8,9.4 13,13.5 18.2,9.4" fill="none" stroke="#0e5468" stroke-width="1.1"/>
      </svg>
      <svg viewBox="0 0 26 26" aria-label="Social profile">
        <circle cx="13" cy="13" r="12" fill="none" stroke="#fff" stroke-width="1.2"/>
        <circle cx="13" cy="13" r="6.5" fill="#fff"/>
      </svg>
      <svg viewBox="0 0 26 26" aria-label="Social profile">
        <circle cx="13" cy="13" r="12" fill="none" stroke="#fff" stroke-width="1.2"/>
        <circle cx="13" cy="13" r="6.5" fill="#fff"/>
      </svg>
    </div>

    <div class="contact-lines">
      <p>(441) 582-6197</p>
      <p>cvnelectricalsoultions@mailventra.com</p>
      <p>@cvnelectricalsolutions</p>
    </div>
  </section>

  <section class="card card--back">
    <div class="brand">
      <span class="brand-mark"></span>
      <span class="brand-name">Corvane<br>Electrical<br>Solutions</span>
    </div>
    <ul class="services">
      <li>Electrical Construction &amp; Maintenance</li>
      <li>LED Lighting &amp; Automation</li>
      <li>Life Safety Systems(Fire Alarm / Security)</li>
      <li>Data &amp; Communication</li>
    </ul>
  </section>
</body>
</html>
```